New Business Card Design for Houston-based Office Building Association

We need a business card design for our membership association in Houston known at Houston TREVA (Houston Tower Lessors & Operators Guild). Our members are office building managers and vendors in the commercial real estate industry. Any building imagery should be of office buildings, skyscrapers, skylines, etc. (Please do NOT use houses or residential homes.) The final design should be clean and cohesive utilizing our logo and branding. I've attached our logos, branding guide, and the information to be included on the business cards.

Target Market(s)

Professionals in office buildings and commercial real estate. Our market is conservative, modern and upmarket.

Contact Information for Business Card

Should include: name, title, email, direct phone number, cell phone number, address, and possibly website. Our address is 14 Larkmont Court, Suite 200, Houston TX 77052. Our website is houstontreva.example. Other fields should be editable for each employee.

Colors
ffffff
33b8a4
86cfc6
00a990

Requirements
Must have
• Clean, professional, modern, look, integrating our branding, logo and colors. Our logo font is Gotham Light and signature color is PMS color Pantone 2401C (hex code 40a89d.) Our accent color is PMS color Pantone Cool Gray 10C (hex code: 636466)
Should not have
• NO imagery of homes or residential houses. We represent commercial real estate/office buildings only.

```html
<!DOCTYPE html>
<html lang="en">
<head>
<meta charset="utf-8">
<title>Houston TREVA — Business Card</title>
<link rel="stylesheet" href="https://fonts.googleapis.com/css2?family=Source+Sans+3:wght@400;600&display=swap">
<style>
  :root {
    --stage: #000000;
    --paper: #ffffff;
    --brand-teal: #3daa9e;
    --accent-gray: #636466;
    --ink: #222222;
    --divider: #c9c9c9;
  }
  html, body {
    margin: 0;
    padding: 0;
    width: 1200px;
    height: 900px;
    overflow: hidden;
    background: var(--stage);
  }
  .stage {
    position: relative;
    width: 1200px;
    height: 900px;
  }
  .card {
    position: absolute;
    top: 275px;
    width: 477px;
    height: 293px;
    box-sizing: border-box;
  }
  .card-front {
    left: 116px;
    background: var(--paper);
    border-radius: 0 62px 0 62px;
  }
  .card-back {
    left: 622px;
    top: 276px;
    height: 292px;
    background: var(--brand-teal);
    border-radius: 62px 0 62px 0;
  }
  .brand-mark {
    position: absolute;
    left: 29px;
    top: 27px;
    width: 76px;
    height: 76px;
    border-radius: 50%;
    background: var(--brand-teal);
  }
  .brand-divider {
    position: absolute;
    left: 124px;
    top: 33px;
    width: 1px;
    height: 65px;
    background: var(--divider);
  }
  .org-name {
    position: absolute;
    left: 140px;
    top: 49px;
    margin: 0;
    font-family: "Source Sans 3", sans-serif;
    font-weight: 600;
    font-size: 26px;
    line-height: 32px;
    color: var(--accent-gray);
    white-space: nowrap;
  }
  .person {
    position: absolute;
    left: 29px;
    top: 134px;
    font-family: "Source Sans 3", sans-serif;
  }
  .person-name {
    margin: 0;
    font-weight: 600;
    font-size: 19px;
    line-height: 22px;
    color: var(--brand-teal);
  }
  .person-title {
    margin: 0;
    font-weight: 400;
    font-size: 14px;
    line-height: 18px;
    color: var(--ink);
  }
  .contact-list {
    position: absolute;
    right: 26px;
    top: 168px;
    margin: 0;
    padding: 0;
    list-style: none;
    font-family: "Source Sans 3", sans-serif;
    font-size: 13.5px;
    color: var(--ink);
  }
  .contact-item {
    display: flex;
    justify-content: flex-end;
    align-items: center;
    height: 19.7px;
    white-space: nowrap;
  }
  .contact-icon {
    width: 10px;
    height: 10px;
    margin-left: 6px;
    fill: var(--brand-teal);
  }
  .address {
    position: absolute;
    right: 26px;
    top: 251px;
    margin: 0;
    font-family: "Source Sans 3", sans-serif;
    font-size: 13.5px;
    font-style: normal;
    color: var(--ink);
    white-space: nowrap;
  }
  .back-name {
    position: absolute;
    left: 96px;
    top: 116px;
    margin: 0;
    font-family: "Source Sans 3", sans-serif;
    font-weight: 400;
    font-size: 46px;
    line-height: 56px;
    color: var(--paper);
    white-space: nowrap;
  }
</style>
</head>
<body>
<main class="stage">
  <section class="card card-front" aria-label="Card front">
    <span class="brand-mark" aria-hidden="true"></span>
    <span class="brand-divider" aria-hidden="true"></span>
    <h1 class="org-name">Houston TREVA</h1>

    <div class="person">
      <p class="person-name">Daniel Harper</p>
      <p class="person-title">Managing Director</p>
    </div>

    <ul class="contact-list">
      <li class="contact-item">(713) 555-0142
        <svg class="contact-icon" viewBox="0 0 10 10" aria-hidden="true"><path d="M2.2 0.6l1.5 1.9-0.9 1.1c0.6 1.3 1.5 2.2 2.8 2.8l1.1-0.9 1.9 1.5-0.9 1.7C4.6 8.6 1.4 5.4 0.5 1.5z"/></svg>
      </li>
      <li class="contact-item">713-555-0187
        <svg class="contact-icon" viewBox="0 0 10 10" aria-hidden="true"><path d="M2.5 0h5v10h-5zM3.4 1v7h3.2V1zM4.6 8.5h0.8v0.7h-0.8z" fill-rule="evenodd"/></svg>
      </li>
      <li class="contact-item">info@houstontreva.example
        <svg class="contact-icon" viewBox="0 0 10 10" aria-hidden="true"><path d="M0 2h10v6H0z"/><path d="M0.6 2.6L5 5.8l4.4-3.2" stroke="#fff" stroke-width="0.8" fill="none"/></svg>
      </li>
      <li class="contact-item">www.houstontreva.example
        <svg class="contact-icon" viewBox="0 0 10 10" aria-hidden="true"><circle cx="5" cy="5" r="4.8"/><path d="M2 3.5c1 0 1.5 1 2.5 1s0.5 1.5 1.5 2" stroke="#fff" stroke-width="0.9" fill="none"/></svg>
      </li>
    </ul>

    <address class="address">14 Larkmont Court, Suite 200, Houston TX 77052</address>
  </section>

  <section class="card card-back" aria-label="Card back">
    <p class="back-name">Houston TREVA</p>
  </section>
</main>
</body>
</html>
```